Design logo, business cards, and web page for new web and bi development consulting company

I've started a Web and Business Intelligence development consulting company. We develop on Quorvantel's stack, Veltrix Studio and Stratalyn Server. We develop responsive web sites and business intelligence platforms. I plan on focusing on small to medium sized business as my client base. I need a logo, business cards, and a one page web site. We will do more with the web site with you in the next six months if the business survives. The name of the company is Belvorq Linkage Solutions, Belvorq for short.

Target Market(s)

small to medium sized businesses

Industry/Entity Type

Business

Contact Information for Business Card

logo
name
title
email
phone

Logo Text

Belvorq Linkage Solutions - web and data solutions

Coding

Coded - Design and coding required

Number of Pages Required

1 page

Font styles to use
Sans Serif

Colors
0355a3
0092cd
00a88f
6b449b

Requirements
Nice to have
• web and data solutions

```html
<!DOCTYPE html>
<html lang="en">
<head>
<meta charset="utf-8">
<title>Belvorq Linkage Solutions</title>
<link href="https://fonts.googleapis.com/css2?family=Open+Sans:ital,wght@0,400;0,600;0,700;1,600&display=swap" rel="stylesheet">
<style>
:root{
  --blue:#0355a3;
  --sky:#0092cd;
  --teal:#00a88f;
  --ink:#222;
  --body:#444;
  --white:#fff;
  --footer:#252525;
  --grey:#7a7a7a;
}
*{margin:0;padding:0;box-sizing:border-box}
html,body{width:1200px;height:2344px;overflow:hidden}
body{position:relative;font-family:"Open Sans",Arial,sans-serif;color:var(--ink);background:var(--white)}
.abs{position:absolute}
.topbar{left:0;top:0;width:1200px;height:35px;background:var(--blue);color:var(--white);font-size:13px}
.topbar .contact{left:57px;top:8px}
.topbar .account{right:50px;top:10px;font-size:11.5px;letter-spacing:.5px}
.topbar .account span{margin:0 8px}
.header{left:0;top:35px;width:1200px;height:102px;border-bottom:4px solid var(--teal)}
.brand{left:52px;top:38px;display:flex;align-items:center;gap:10px;font-size:20px;font-weight:600;color:var(--blue);line-height:1}
.brand i{display:block;width:22px;height:22px;background:var(--blue)}
.nav{left:418px;top:33px;display:flex;font-size:13.5px;font-weight:600;letter-spacing:.6px}
.nav a{color:#333;text-decoration:none;padding:6px 12px 7px;line-height:18px}
.nav a.active{background:var(--teal);color:var(--white)}
.social{left:988px;top:34px;display:flex;gap:6px}
.social i{display:block;width:27px;height:27px;border-radius:50%;background:var(--grey)}
.hero{left:0;top:140px;width:1200px;height:422px;background:linear-gradient(100deg,#3c4a5c 0%,#6a7a8c 25%,#2c3d52 50%,#8c97a4 75%,#c9ccd0 100%)}
.hero .shade{inset:0;background:rgba(10,20,35,.35)}
.hero h1{left:0;width:1200px;top:102px;text-align:center;color:var(--white);font-size:28px;font-weight:600;letter-spacing:.5px}
.hero p{left:180px;width:840px;top:156px;text-align:center;color:var(--white);font-size:12.5px;line-height:29px}
.btn{display:flex;align-items:center;justify-content:center;background:linear-gradient(#f2f2f2,#cfcfcf);color:#333;font-size:15px;border-radius:2px}
.hero .btn{left:508px;top:245px;width:187px;height:45px;letter-spacing:1px;font-weight:600}
.dots{display:flex;gap:9px}
.dots i{display:block;width:15px;height:15px;border-radius:50%;background:var(--white)}
.dots i.on{background:var(--teal);border:2px solid var(--white)}
.hero .dots{left:556px;top:388px}
.welcome h2{left:0;width:1200px;top:603px;text-align:center;font-size:28px;font-weight:400;color:var(--ink)}
.welcome h3{left:0;width:1200px;top:648px;text-align:center;font-size:18px;font-style:italic;font-weight:600;color:var(--teal)}
.welcome p{left:120px;width:960px;top:686px;text-align:center;font-size:12.5px;line-height:23px;color:var(--body)}
.skill{width:210px;height:210px;border:4px solid var(--teal);border-radius:50%;top:764px}
.skill .icon{left:67px;top:52px;width:68px;height:60px;border-radius:6px}
.skill .label{left:0;width:202px;top:134px;text-align:center;font-size:14.5px;font-weight:600;color:#111}
.featured{left:0;top:1075px;width:1200px;height:401px;background:radial-gradient(circle at 20% 30%,#1f6fd0 0%,rgba(31,111,208,0) 35%),radial-gradient(circle at 85% 70%,#1a63c4 0%,rgba(26,99,196,0) 30%),linear-gradient(180deg,#0d3f93,#082b6e)}
.featured h2{left:0;width:1200px;top:20px;text-align:center;color:var(--white);font-size:27px;font-weight:600}
.featured .work{left:148px;top:98px;width:439px;height:259px;border:4px solid #e8e8e8;border-radius:4px;background:linear-gradient(160deg,#8fb0c7,#c9b6a2 45%,#6f8f4c 80%,#a43a2e)}
.featured h4{left:644px;top:118px;color:var(--white);font-size:22px;font-weight:400}
.featured p{left:644px;top:165px;width:400px;color:var(--white);font-size:12.5px;line-height:23px}
.featured .btn{left:644px;top:280px;width:187px;height:47px}
.arrow{top:182px}
.testimonials{left:0;top:1476px;width:1200px;height:304px;background:var(--teal)}
.testimonials .quote{left:576px;top:14px}
.testimonials h2{left:0;width:1200px;top:60px;text-align:center;color:var(--white);font-size:28px;font-weight:600}
.testimonials p{left:200px;width:800px;top:115px;text-align:center;color:var(--white);font-size:12.5px;line-height:22px}
.testimonials .author{left:500px;width:200px;top:231px;display:flex;align-items:center;gap:14px;color:var(--white);font-size:12px;font-weight:700}
.testimonials .author b{flex:1;height:1px;background:rgba(255,255,255,.6)}
.testimonials .dots{left:552px;top:271px}
.testimonials .dots i.on{background:var(--teal)}
.clients h2{left:50px;top:1804px;font-size:28px;font-weight:400}
.client{top:1890px;width:170px;display:flex;align-items:center;justify-content:center;gap:10px;font-size:17px;font-weight:600;color:#555}
.client i{display:block;width:36px;height:36px;border-radius:50%;background:#8a8a8a}
.footer{left:0;top:2000px;width:1200px;height:297px;background:var(--footer);color:var(--white)}
.col{top:38px}
.col h5{font-size:20px;font-weight:400;margin-bottom:12px}
.col a{display:block;color:var(--white);text-decoration:none;font-size:11.5px;line-height:28px;padding-left:3px}
.divider{top:20px;width:1px;height:245px;background:#3a3a3a}
.field{left:847px;width:214px;border:1px solid #8a8a8a;border-radius:3px;font-size:11.5px;padding:9px 11px}
.submit{left:847px;top:226px;width:214px;height:36px;background:var(--teal);border-radius:3px;display:flex;align-items:center;justify-content:center;font-size:14px;font-weight:700}
.copyright{left:0;top:2297px;width:1200px;height:47px;background:var(--teal);color:var(--white);font-size:11.5px;padding:16px 0 0 120px}
</style>
</head>
<body>

<div class="abs topbar">
  <div class="abs contact">Call Us Today! 1-800-555-0142 | 1-800-555-0187|hello@belvorq.example</div>
  <div class="abs account">LOGIN<span>|</span>REGISTER<span>|</span>CONTACT US</div>
</div>

<header class="abs header">
  <div class="abs brand"><i></i>Belvorq Linkage Solutions</div>
  <nav class="abs nav">
    <a class="active">HOME</a><a>ABOUT</a><a>SERVICES</a><a>PRODUCTS</a><a>BLOG</a><a>NEWS</a><a>CAREERS</a>
  </nav>
  <div class="abs social"><i></i><i></i><i></i><i></i><i></i></div>
</header>

<section class="abs hero" role="img" aria-label="Business people shaking hands in an office">
  <div class="abs shade"></div>
  <h1 class="abs">BUSINESS INTELLIGENCE DEVELOPMENT</h1>
  <p class="abs">Aenean sollicitudin, lorem quis bibendum auctor, nisi elit consequat ipsum, nec sagittis sem nibh id elit. Duis sed odio sit amet nibh vulputate cursus a sit amet mauris. Morbi accumsan ipsum velit.</p>
  <div class="abs btn">LEARN&nbsp; MORE</div>
  <div class="abs dots"><i class="on"></i><i></i><i></i><i></i></div>
</section>

<section class="welcome">
  <h2 class="abs">Welcome to&nbsp; Belvorq Linkage Solutions</h2>
  <h3 class="abs">Web and Business Intelligence development consulting</h3>
  <p class="abs">We develop on Quorvantel's stack, Veltrix Studio and Stratalyn Server.Proin gravida nibh vel velit auctor aliquet. Aenean sollicitudin, lorem quis bibendum auctor, nisi elit consequat ipsum, nec sagittis sem nibh id elit. Duis sed odio sit amet nibh vulputate cursus a sit amet mauris.</p>
  <div class="abs skill" style="left:207px">
    <div class="abs icon" role="img" aria-label="Network device icon" style="background:linear-gradient(#e8e8e8,#8c8c8c)"></div>
    <div class="abs label">QUORVANTEL'S STACK</div>
  </div>
  <div class="abs skill" style="left:493px">
    <div class="abs icon" role="img" aria-label="Server rack icon" style="background:linear-gradient(#9aa3ad,#3e4650)"></div>
    <div class="abs label">VELTRIX STUDIO</div>
  </div>
  <div class="abs skill" style="left:781px">
    <div class="abs icon" role="img" aria-label="Database icon" style="background:linear-gradient(#555,#111)"></div>
    <div class="abs label">STRATALYN SERVER</div>
  </div>
</section>

<section class="abs featured">
  <h2 class="abs">Featured Works</h2>
  <svg class="abs arrow" style="left:50px" width="20" height="30" viewBox="0 0 20 30"><path d="M15 4 5 15l10 11" fill="none" stroke="#fff" stroke-width="3"/></svg>
  <svg class="abs arrow" style="left:1130px" width="20" height="30" viewBox="0 0 20 30"><path d="M5 4l10 11L5 26" fill="none" stroke="#fff" stroke-width="3"/></svg>
  <div class="abs work" role="img" aria-label="Screenshot of a featured exhibition display project"></div>
  <h4 class="abs">Lorem ipsum dolor sit</h4>
  <p class="abs">Proin gravida nibh vel velit auctor aliquet. Aenean sollicitudin, lorem quis bibendum auctor, nisi elit consequat ipsum, nec sagittis sem nibh id elit. Duis sed odio sit amet nibh vulputate cursus a sit amet mauris. Morbi accumsan ipsum velit.</p>
  <div class="abs btn">Live Demo</div>
</section>

<section class="abs testimonials">
  <svg class="abs quote" width="48" height="30" viewBox="0 0 48 30"><path d="M4 28V16L12 2h6l-5 14h6v12zM26 28V16L34 2h6l-5 14h6v12z" fill="#7fd6c8"/></svg>
  <h2 class="abs">Testimonials</h2>
  <p class="abs">Proin gravida nibh vel velit auctor aliquet. Aenean sollicitudin, lorem quis bibendum auctor, nisi elit consequat ipsum, nec sagittis sem nibh id elit. Duis sed odio sit amet nibh vulputate cursus a sit amet mauris. Morbi accumsan ipsum velit. Nam nec tellus a odio tincidunt auctor a ornare odio. Sed non&nbsp; mauris vitae erat consequat auctor eu in elit. Class aptent taciti sociosqu ad litora torquent per conubia nostra, per inceptos himenaeos. Mauris in erat justo. Nullam ac urna eu felis dapibus condimentum sit amet a augue.</p>
  <div class="abs author"><b></b>MARA<b></b></div>
  <div class="abs dots"><i class="on"></i><i></i><i></i><i></i></div>
</section>

<section class="clients">
  <h2 class="abs">Our Clients</h2>
  <div class="abs client" style="left:48px"><i></i>Ternwick</div>
  <div class="abs client" style="left:234px"><i></i>Oravia</div>
  <div class="abs client" style="left:404px"><i></i>Fennlow</div>
  <div class="abs client" style="left:592px"><i></i>Qualtrin</div>
  <div class="abs client" style="left:784px"><i></i>Dovestra</div>
  <div class="abs client" style="left:967px"><i></i>Marrowby</div>
</section>

<footer class="abs footer">
  <div class="abs col" style="left:119px">
    <h5>MAIN LINKS</h5>
    <a>HOME</a><a>SHOP</a><a>FEATURES &amp; BENEFITS</a><a>VIDEO</a><a>USES</a><a>ADVANTAGES</a><a>TESTIMONIALS</a>
  </div>
  <div class="abs divider" style="left:289px"></div>
  <div class="abs col" style="left:340px">
    <h5>INFORMATION</h5>
    <a>CONTACT US</a><a>TESTIMONIALS</a><a>PRESS</a><a>COMMUNITY</a><a>TERMS &amp; CONDITIONS</a><a>PRIVACY POLICY</a>
  </div>
  <div class="abs divider" style="left:598px"></div>
  <div class="abs col" style="left:631px">
    <h5>MORE LINKS</h5>
    <a>HOW THEY WORK</a><a>VIDEO</a><a>INSTRUCTIONS</a><a>FAQS</a><a>EDUCATION</a>
  </div>
  <div class="abs divider" style="left:790px"></div>
  <div class="abs col" style="left:844px"><h5>CONTACT US</h5></div>
  <div class="abs field" style="top:78px;height:35px">NAME</div>
  <div class="abs field" style="top:131px;height:77px">MESSAGE (REQUIRED)</div>
  <div class="abs submit">SUBMIT NOW</div>
</footer>

<div class="abs copyright">Copyright © 2015 Belvorq. All rights reserved.</div>

</body>
</html>
```